Aesthetics Company Flyer (description of services)

We need a 5.5"x8.5" flyer describing the services we offer at velvet horizon aesthetics. We are an aesthetics company located in Conroe TX. Our products and services can be found at www.vhaesthetics-demo.com/services . We would like to see designs that are cohesive with our brand and website: https://www.vhaesthetics-demo.com/

```html
<!DOCTYPE html>
<html lang="en">
<head>
<meta charset="utf-8">
<title>Velvet Horizon Aesthetics – Services Flyer</title>
<link href="https://fonts.googleapis.com/css2?family=Oswald:wght@300;400;500&family=Raleway:wght@400;500&display=swap" rel="stylesheet">
<style>
  :root{
    --page:#ffffff;
    --paper:#f8f1f6;
    --lilac:#d1b8f2;
    --lilac-soft:#ebdff5;
    --lilac-line:#c6a7ef;
    --lilac-text:#c3a0ee;
    --ink:#1e1a1d;
    --ink-soft:#3a3438;
    --white:#ffffff;
  }
  *{margin:0;padding:0;box-sizing:border-box}
  html,body{width:1200px;height:1000px;overflow:hidden;background:var(--page)}
  .flyer{position:absolute;left:350px;top:113px;width:500px;height:774px;background:var(--paper);font-family:"Raleway",sans-serif;color:var(--ink)}
  .abs{position:absolute}
  .brand-mark{left:0;top:22px;width:500px;text-align:center}
  .brand-dot{width:44px;height:44px;border-radius:50%;border:1.5px solid var(--ink-soft);margin:0 auto 10px}
  .brand-name{font-family:"Oswald",sans-serif;font-weight:400;font-size:15px;letter-spacing:3px;text-transform:uppercase;color:var(--ink-soft);line-height:1.25}
  .headline{left:0;top:131px;width:500px;text-align:center;font-family:"Oswald",sans-serif;font-weight:500;font-size:24px;letter-spacing:.3px}
  .intro{left:30px;top:165px;width:440px;text-align:center;font-size:11.5px;line-height:14px;color:var(--ink-soft);white-space:nowrap}
  .hero-band{left:203px;top:214px;width:274px;height:185px;background:var(--lilac);border:1px solid var(--lilac-line)}
  .hatch{left:21px;top:214px;width:44px;height:185px}
  .photo-frame{left:35px;top:227px;width:214px;height:159px;background:var(--white);border:1px solid var(--lilac-line)}
  .photo-main{left:44px;top:235px;width:197px;height:141px;background:linear-gradient(100deg,#c9986f 0%,#e6c7a8 35%,#3a3534 60%,#2a2727 100%)}
  .quote-frame{left:197px;top:253px;width:106px;height:105px;background:var(--white)}
  .quote{left:204px;top:260px;width:92px;height:91px;background:var(--paper);padding:4px 0 0 3px;font-family:"Oswald",sans-serif;font-weight:400;font-size:14px;line-height:18px;text-transform:uppercase;color:var(--ink-soft);white-space:nowrap;overflow:hidden}
  .quote .accent{display:block;margin-top:9px;color:var(--lilac-text)}
  .portrait-frame{left:339px;top:253px;width:105px;height:105px;background:var(--white)}
  .portrait{left:346px;top:260px;width:91px;height:91px;background:linear-gradient(180deg,#b9c1cf 0%,#7a6a5e 50%,#eceae8 100%)}
  .banner{left:23px;top:408px;width:454px;height:33px}
  .banner-title{left:29px;top:412px;font-family:"Oswald",sans-serif;font-weight:500;font-size:17.5px;color:var(--ink);white-space:nowrap}
  .banner-handle{left:243px;top:412px;font-family:"Oswald",sans-serif;font-weight:400;font-size:17.5px;color:var(--ink-soft);letter-spacing:.3px;white-space:nowrap}
  .section-head{left:23px;width:231px;height:26px;border:1.5px solid var(--lilac-line);background:var(--paper);padding-left:5px;font-family:"Oswald",sans-serif;font-weight:500;font-size:17px;line-height:23px}
  .chips{left:23px;width:231px;display:flex;flex-direction:column;gap:6px}
  .chip-row{display:flex;gap:6px;height:21px}
  .chip{flex:1 1 auto;display:flex;align-items:center;justify-content:center;padding:0 4px;font-size:12.5px;white-space:nowrap;background:var(--lilac-soft)}
  .chip.is-accent{background:var(--lilac)}
  .gallery{left:278px;top:455px;width:199px;height:197px;background:var(--lilac-soft)}
  .tile{width:87px;height:87px}
  .tile-a{left:286px;top:463px;background:linear-gradient(135deg,#d9a889,#8fb7d4)}
  .tile-b{left:381px;top:463px;background:linear-gradient(135deg,#e8d4c6,#f3ece8)}
  .tile-c{left:286px;top:558px;background:linear-gradient(135deg,#d8c15a,#3a3535)}
  .tile-d{left:381px;top:558px;background:linear-gradient(135deg,#e3bda4,#f0dccc)}
  .contact{left:282px;top:658px;width:215px;font-size:11.5px;line-height:16px;color:var(--ink-soft);list-style:none;white-space:nowrap}
  .contact li{display:flex;gap:6px;align-items:flex-start}
  .contact svg{flex:none;width:11px;height:11px;margin-top:2px}
</style>
</head>
<body>
<main class="flyer">
  <div class="abs brand-mark">
    <div class="brand-dot"></div>
    <div class="brand-name">Velvet Horizon<br>Aesthetics</div>
  </div>

  <h1 class="abs headline">Discover Velvet Horizon Aesthetics</h1>
  <p class="abs intro">Velvet Horizon Aesthetics is your trusted aesthetics partner<br>in Conroe, TX. Our mission is to enhance your natural beauty and<br>boost your confidence through personalized treatments.</p>

  <div class="abs hero-band"></div>
  <svg class="abs hatch" viewBox="0 0 44 185" aria-hidden="true">
    <g stroke="#9a9398" stroke-width="0.8">
      <line x1="0" y1="35" x2="44" y2="0"/><line x1="0" y1="55" x2="44" y2="20"/>
      <line x1="0" y1="75" x2="44" y2="40"/><line x1="0" y1="95" x2="44" y2="60"/>
      <line x1="0" y1="115" x2="44" y2="80"/><line x1="0" y1="135" x2="44" y2="100"/>
      <line x1="0" y1="155" x2="44" y2="120"/><line x1="0" y1="175" x2="44" y2="140"/>
      <line x1="0" y1="185" x2="44" y2="160"/>
    </g>
  </svg>
  <div class="abs photo-frame"></div>
  <div class="abs photo-main" role="img" aria-label="Photo of two smiling women with glowing skin on a dark background"></div>
  <div class="abs quote-frame"></div>
  <div class="abs quote">We change<br>the world<span class="accent">One beautiful<br>face at a time</span></div>
  <div class="abs portrait-frame"></div>
  <div class="abs portrait" role="img" aria-label="Portrait of the clinic's practitioner in a white coat"></div>

  <svg class="abs banner" viewBox="0 0 454 33" aria-hidden="true">
    <polygon points="0.5,0.5 207,0.5 216,16.5 207,32.5 0.5,32.5" fill="#d1b8f2" stroke="#c6a7ef"/>
    <polygon points="200,0.5 453.5,0.5 453.5,32.5 200,32.5 209,16.5" fill="none" stroke="#c6a7ef" stroke-width="1.2"/>
  </svg>
  <div class="abs banner-title">Services &amp; Product We Offer</div>
  <div class="abs banner-handle">@ Velvet Horizon</div>

  <h2 class="abs section-head" style="top:456px">Services</h2>
  <div class="abs chips" style="top:486px">
    <div class="chip-row"><span class="chip">Glutathione</span><span class="chip is-accent">Myers’ Cocktail</span></div>
    <div class="chip-row"><span class="chip is-accent">Post Workout Recovery</span><span class="chip">Hangover</span></div>
    <div class="chip-row"><span class="chip">Migraine Rescue</span><span class="chip is-accent">Quench Hydrator</span></div>
    <div class="chip-row"><span class="chip is-accent">Velvet Glow</span><span class="chip">Immunity Booster</span></div>
    <div class="chip-row"><span class="chip">Peak Athletic Performance</span><span class="chip is-accent">NAD+</span></div>
  </div>

  <h2 class="abs section-head" style="top:633px">Products</h2>
  <div class="abs chips" style="top:664px">
    <div class="chip-row"><span class="chip is-accent">Semaglutide</span><span class="chip">Dermal Fillers</span></div>
    <div class="chip-row"><span class="chip">Fibrin Growth Factor</span><span class="chip is-accent">Micro Pen</span></div>
    <div class="chip-row"><span class="chip is-accent">Chemical Peels</span><span class="chip">Neurotoxin</span></div>
  </div>

  <div class="abs gallery"></div>
  <div class="abs tile tile-a" role="img" aria-label="Filler injection treatment on a client's cheek"></div>
  <div class="abs tile tile-b" role="img" aria-label="Client receiving a facial injection"></div>
  <div class="abs tile tile-c" role="img" aria-label="Yellow chemical peel mask being applied"></div>
  <div class="abs tile tile-d" role="img" aria-label="Growth factor serum treatment on skin"></div>

  <ul class="abs contact">
    <li><svg viewBox="0 0 12 12"><path d="M2.5 1l2 2.5-1 1.2a6 6 0 0 0 3.8 3.8l1.2-1 2.5 2-1 1.5C5 11 1 7 1 2z" fill="none" stroke="#3a3438" stroke-width="0.9"/></svg><span>936 555 0142</span></li>
    <li><svg viewBox="0 0 12 12"><rect x="0.8" y="2" width="10.4" height="8" fill="none" stroke="#3a3438" stroke-width="0.9"/><path d="M1 2.5l5 4 5-4" fill="none" stroke="#3a3438" stroke-width="0.9"/></svg><span>hello@vhaesthetics-demo.com</span></li>
    <li><svg viewBox="0 0 12 12"><circle cx="6" cy="6" r="5" fill="none" stroke="#3a3438" stroke-width="0.9"/><ellipse cx="6" cy="6" rx="2.2" ry="5" fill="none" stroke="#3a3438" stroke-width="0.9"/><line x1="1" y1="6" x2="11" y2="6" stroke="#3a3438" stroke-width="0.9"/></svg><span>https://www.vhaesthetics-demo.com</span></li>
    <li><svg viewBox="0 0 12 12"><path d="M6 11.5S2 7.2 2 4.6a4 4 0 0 1 8 0c0 2.6-4 6.9-4 6.9z" fill="none" stroke="#3a3438" stroke-width="0.9"/><circle cx="6" cy="4.6" r="1.4" fill="none" stroke="#3a3438" stroke-width="0.9"/></svg><span>2150 Cedar Bend Rd #210<br>Magnolia, TX 77355<br>(Across from Lakeside Cinema)</span></li>
  </ul>
</main>
</body>
</html>
```